"End of year wishes" - Electronic card

Quenlax is a regulatory consulting company in the cosmetic sector. We provide premium services and have 12 years of experience.
Please visit our website for more information: https://quenlax.example
Like every year, we would like to send an electronic design to our clients and partners to wish them happy holidays. This year, we would like to share two good news with them: offer them a surprise (to be revealed later on) and invite them to visit our new brand new website. We relay on your talent and imagination for the design! We need something very professional, serious, beautiful and in line with our graphic layout (see our company website)

Target Market(s)

cosmetic brands

Industry/Entity Type

Cosmetics

Requirements
Must have
• The following statement should be included to the design:

We wish you a Happy Holiday and a Marvelous New Year 2021!
As December is the month of giving, we have a surprise for you. Please contact your dedicated Account Manager to find out more!

Good news never comes alone, we've also updated our website in order to serve you better. We hope you like it as much as we do.
Please enjoy the experience: www.quenlax.example

```html
<!DOCTYPE html>
<html lang="en">
<head>
<meta charset="utf-8">
<title>Quenlax – Season's Greetings 2021</title>
<link rel="stylesheet" href="https://fonts.googleapis.com/css2?family=Alegreya+Sans:wght@400;500;800&display=swap">
<style>
  :root {
    --paper: #ffffff;
    --ink: #0a0a0a;
    --green-deep: #3fbf00;
    --green-mid: #7ee21a;
    --green-light: #c9f28a;
    --green-pale: #eefbd6;
    --leaf: #8cc63f;
    --gift-orange: #f7b52a;
    --gift-yellow: #f2ee1c;
  }
  * { margin: 0; padding: 0; box-sizing: border-box; }
  html, body {
    width: 1200px;
    height: 900px;
    overflow: hidden;
    background: var(--paper);
  }
  .card {
    position: relative;
    width: 1200px;
    height: 900px;
    overflow: hidden;
    background: var(--paper);
    font-family: "Alegreya Sans", sans-serif;
    color: var(--ink);
  }
  .card__backdrop,
  .card__foliage,
  .card__fireworks,
  .card__gifts {
    position: absolute;
  }
  .card__backdrop { left: 0; top: 0; width: 1200px; height: 900px; }
  .card__foliage { left: 0; top: 0; width: 300px; height: 340px; }
  .card__fireworks { left: 850px; top: 0; width: 350px; height: 245px; }
  .card__gifts { left: 16px; top: 775px; width: 250px; height: 125px; }

  .greeting {
    position: absolute;
    left: 0;
    top: 208px;
    width: 1208px;
    text-align: center;
    font-size: 32px;
    line-height: 47px;
    font-weight: 500;
  }
  .greeting__headline { font-size: 32px; }
  .greeting__year {
    font-size: 39px;
    line-height: 50px;
    margin-bottom: 2px;
  }
  .greeting__block + .greeting__block { margin-top: 38px; }

  .brand {
    position: absolute;
    right: 36px;
    top: 772px;
    font-family: "Alegreya Sans", sans-serif;
    font-weight: 800;
    font-size: 96px;
    line-height: 1;
    letter-spacing: 1px;
    color: var(--ink);
  }
</style>
</head>
<body>
<main class="card">
  <svg class="card__backdrop" viewBox="0 0 1200 900" role="img" aria-label="Green watercolour wash spreading across the card">
    <defs>
      <radialGradient id="wash" cx="0.5" cy="0.48" r="0.62">
        <stop offset="0" stop-color="var(--green-deep)"/>
        <stop offset="0.45" stop-color="var(--green-mid)"/>
        <stop offset="0.8" stop-color="var(--green-light)"/>
        <stop offset="1" stop-color="var(--green-pale)"/>
      </radialGradient>
    </defs>
    <path fill="url(#wash)" d="M170 60 C320 10 520 40 660 20 C820 0 960 60 1060 160 C1160 250 1200 380 1170 520 C1150 640 1060 700 1080 800 C1000 880 760 900 560 880 C380 870 200 860 110 770 C40 700 30 560 40 440 C50 300 60 150 170 60 Z"/>
  </svg>

  <svg class="card__foliage" viewBox="0 0 300 340" role="img" aria-label="Green leafy branches in the top left corner">
    <defs>
      <linearGradient id="foliage" x1="0" y1="0" x2="1" y2="1">
        <stop offset="0" stop-color="var(--leaf)"/>
        <stop offset="1" stop-color="var(--green-mid)" stop-opacity="0"/>
      </linearGradient>
    </defs>
    <path fill="url(#foliage)" d="M0 0 H290 C260 120 210 220 150 330 C90 300 30 270 0 240 Z"/>
  </svg>

  <svg class="card__fireworks" viewBox="0 0 350 245" role="img" aria-label="Green firework burst with confetti in the top right corner">
    <defs>
      <radialGradient id="burst" cx="0.62" cy="0.4" r="0.6">
        <stop offset="0" stop-color="var(--green-mid)" stop-opacity="0.55"/>
        <stop offset="1" stop-color="var(--green-mid)" stop-opacity="0"/>
      </radialGradient>
    </defs>
    <rect width="350" height="245" fill="url(#burst)"/>
  </svg>

  <svg class="card__gifts" viewBox="0 0 250 125" role="img" aria-label="Two open gift boxes with ribbons and confetti">
    <rect x="20" y="45" width="120" height="80" fill="var(--gift-orange)"/>
    <rect x="170" y="55" width="80" height="70" fill="var(--gift-yellow)"/>
  </svg>

  <section class="greeting">
    <div class="greeting__block">
      <p class="greeting__headline">We wish you a Happy Holidays and Prosperous</p>
      <p class="greeting__year">New Year 2021!</p>
      <p>As December is the month of giving, we have a<br>surprise for you! Please contact your dedicated<br>Account Manager to find out more!</p>
    </div>
    <div class="greeting__block">
      <p>Good things come in pairs, our website has been<br>refreshed to serve you better. We hope that you<br>will like it as much as we do.</p>
    </div>
    <div class="greeting__block">
      <p>Please enjoy the experience: https://quenlax.example/</p>
    </div>
  </section>

  <p class="brand">quenlax</p>
</main>
</body>
</html>
```